International Career Development Workshop

I need a Powerpoint revised and designed in a more professional manner for a presentation I will be giving. We are an International Education Company that provides students with Internships Abroad, and are expanding our career development programming to offer more guidance through on-site workshops. I am happy to send along our website to showcase the colors and fonts we use, but we tend to use royal blue, lime green, and white in our color scheme. The final design should communicate opportunity and self-awareness within college students.

Target Market(s)

College Students, University Partners, and International Education Community

Industry/Entity Type

Education

Font styles to use
Sans Serif

Colors
9bcb3b
0355a3
ffffff

Requirements
Must have
• Our logo, our color scheme, a unified, professional theme throughout, Watermark of our logo, thematic sections spread across four sections.
Nice to have
• Videos and graphics
Should not have
• Spelling Errors, sloppy design

```html
<!DOCTYPE html>
<html lang="en">
<head>
<meta charset="utf-8">
<title>Project Title Slide</title>
<link rel="stylesheet" href="https://fonts.googleapis.com/css2?family=Lato:wght@400;700;900&family=Lora:wght@400;700&display=swap">
<style>
  :root {
    --royal-blue: #0355a3;
    --lime: #9bcb3b;
    --white: #ffffff;
    --ink: #3a3a3a;
  }
  * { box-sizing: border-box; margin: 0; padding: 0; }
  html, body { width: 1200px; height: 900px; overflow: hidden; background: var(--white); }
  .slide {
    position: relative;
    width: 1200px;
    height: 900px;
    background: var(--white);
    overflow: hidden;
  }
  .slide-header {
    position: absolute;
    left: 0; top: 0;
    width: 1200px; height: 85px;
    background: var(--royal-blue);
    display: flex;
    align-items: center;
    justify-content: space-between;
    padding: 0 36px 0 33px;
  }
  .slide-title {
    font-family: "Lato", sans-serif;
    font-weight: 900;
    font-size: 39px;
    color: var(--white);
    letter-spacing: 0.2px;
  }
  .brand {
    display: flex;
    align-items: center;
    gap: 12px;
    font-family: "Lato", sans-serif;
    font-weight: 700;
    font-size: 24px;
    color: var(--white);
    text-transform: uppercase;
    letter-spacing: 0.5px;
  }
  .brand-dot {
    width: 40px; height: 40px;
    border-radius: 50%;
    background: var(--white);
  }
  .columns {
    position: absolute;
    top: 150px;
    left: 50px;
    width: 1122px;
    display: flex;
    gap: 72px;
  }
  .column { width: 525px; }
  .column-heading {
    font-family: "Lora", serif;
    font-weight: 700;
    font-size: 31px;
    line-height: 1.2;
    color: var(--royal-blue);
    margin-bottom: 2px;
  }
  .column-text {
    font-family: "Lora", serif;
    font-weight: 400;
    font-size: 22px;
    line-height: 39px;
    color: var(--ink);
    hyphens: auto;
    -webkit-hyphens: auto;
  }
  .column-text + .column-text { margin-top: 39px; }
  .slide-footer {
    position: absolute;
    left: 0; top: 860px;
    width: 1200px; height: 40px;
    background: var(--lime);
    display: flex;
    align-items: center;
    padding-left: 30px;
  }
  .copyright {
    font-family: "Lato", sans-serif;
    font-size: 22px;
    color: var(--white);
  }
</style>
</head>
<body>
<div class="slide">
  <header class="slide-header">
    <h1 class="slide-title">PROJECT TITLE HERE</h1>
    <div class="brand"><span class="brand-dot"></span>Meridian Abroad</div>
  </header>

  <main class="columns">
    <section class="column">
      <h2 class="column-heading">Subtitle Here</h2>
      <p class="column-text">&nbsp;chocolate chocolate cake carrot cake dragée candy canes gummies bear cake icing oat cake jelly chocolate chocolate cake carrot cake dragée candy canes gummies bear Gummies cake icing oat cake jelly chocolate chocolate cake carrot cake dragée candy canes gummies bear cake icing oat cake jelly chocolate chocolate cake carrot cake dragée candy canes gummies bear</p>
      <p class="column-text">Gummies cake icing oat cake jelly chocolate chocolate cake carrot cake dragée candy canes gummies bear cake icing oat cake jelly chocolate chocolate cake carrot cake dragée candy canes gummies bear Gummies cake icing oat</p>
    </section>
    <section class="column">
      <h2 class="column-heading">Subtitle Here</h2>
      <p class="column-text">&nbsp;chocolate chocolate cake carrot cake dragée candy canes gummies bear cake icing oat cake jelly chocolate chocolate cake carrot cake dragée candy canes gummies bear Gummies cake icing oat cake jelly chocolate chocolate cake carrot cake dragée candy canes gummies bear cake icing oat cake jelly chocolate chocolate cake carrot cake dragée candy canes gummies bear</p>
      <p class="column-text">Gummies cake icing oat cake jelly chocolate chocolate cake carrot cake dragée candy canes gummies bear cake icing oat cake jelly chocolate chocolate cake carrot cake dragée candy canes gummies bear Gummies cake icing oat</p>
    </section>
  </main>

  <footer class="slide-footer">
    <p class="copyright">Copyright text here</p>
  </footer>
</div>
</body>
</html>
```